MODERN + COOL Business Card Needed!

SUMMARY
This is for a 40+ year old family business that is transitioning to the 2nd generation and is in real need of a more modern facelift. Ive attached a company logo (I made quickly as an idea with my limited PSD skills) to start off with that you are welcome to change and draw ideas from. Ive also attached some screen shots of cards I like to give you an idea of my preferences.

WHAT WE DO
The company name is Tall Pine HK Ltd. But I prefer to just call it Tall Pine or Tall Pine with Hong Kong as kind of a sub heading on the business card. We own a factory as well as help our customers find factories to make their product. Product I mean, toys 99.9% of the time. Simple old school toys like board games, puzzles, wooden toys, baby/infant toys.

You can say we are a "sourcing" or "trading" or "consulting" company with a factory to help you do it. But since we deal with toys, i like to keep it modern and cool and fun, not serious like managing hedge funds.

WHAT WE ARE LOOKING FOR
A cool, unique looking business card that stands out. In terms of design, something modern and professional. I like darker colored cards and I like colors such as blue/green/dark gray, but am open to other colored themes. I Like bright lime green with gray, always though thats a nice combo. I prefer cards that are all colored and not so much white showing (I think). Ive attached a few screenshots of cards so take a look to get a feel of what I like.

We do alot of wooden stacking games in variety of colors too like Tovra, Lumo, Towerplix (google these to check them out). So designs that sort of resemble stacking or building would be cool but totally not necessary.

In terms of the physical aspects of the card, Im looking for a card a bit different than the standard rectangular shape. Double sided. Little things like having corner(s) be round or different angle instead of square edge I always thought was nice. Its got to be mostly a normal card size, no folding or smaller cards that fit weird in your wallet. No vertical designs. Am open to VERY different/creative shapes (as long as it still fits in a wallet good like a normal buisness card.
Updates

Hi everyone!

Just wanted to write a message to everyone to let them know all submissions are being reviewed or have been reviewed.  If I have not responded with feedback, rest assure your submission was definitely looked at in detail but I either have just been too busy to respond (alot of submissions!), or its on my to be considered list.

I respect and really enjoy receiving everyones creativity and work so I dont want it to go unrecognized - thus this message!  Feel free to submit more ideas if you like until this project ends.  Sometimes some designs just dont click but sometimes they can so you never know!

Thanks again for everyones participation and great work!

~Dev Orr

Target Market(s)

The cards are mainly handed to toy company sourcers and buyers. People I talk to ... say Pelvane for example... might want to make their next edition of Farthingale game with a reputable factory at a good cost so they can sell it to stores at a profit.

So these are the types of people I often try to talk and introduce myself and my company to.

Industry/Entity Type

Building

Colors
acd036
0392cd
00a88e
474747
606060

Requirements
Must have
• Just double sided, not plain rectangle corners, and just cool to look at and catches your eye!

Oh and the obvious business card stuff like place for name, address, number, email, etc.
Nice to have
• Think more modern and fun, not serious and old fashion (thats what we used to be!). Can use the logo I attached and you can definitely alter and change the logo or make a whole new one!

Oh and can definitely use a creative slogan if you like to think of one based on what I described in what we do.
Should not have
• Dont use fonts or text placement that might make "Tall Pine" look like "Tal Lpine"... We arent selling news papers!!

Please nothing related to education since we have the word Pine in the title, thats not our business at all.

Logo and design should not be too heavy on things related to toys, as though thats what we primarily focus on now, what we do may change over time.

```html
<!DOCTYPE html>
<html lang="en">
<head>
<meta charset="utf-8">
<title>Tall Pine Hong Kong – Business Card</title>
<link rel="stylesheet" href="https://fonts.googleapis.com/css2?family=Cabin:wght@400;500;700&display=swap">
<style>
  :root {
    --backdrop: #1c1c1d;
    --card: #3b3b3d;
    --card-deep: #353537;
    --tone-light: #4a4a4d;
    --tone-mid: #414144;
    --lime: #acd036;
    --teal: #00a88e;
    --text-light: #e4e4e4;
    --text-soft: #cfcfcf;
  }
  * { box-sizing: border-box; margin: 0; padding: 0; }
  html, body { width: 1200px; height: 900px; overflow: hidden; }
  body {
    background: var(--backdrop);
    font-family: "Cabin", "Gill Sans", sans-serif;
    display: flex;
    flex-direction: column;
    align-items: center;
    justify-content: center;
    gap: 40px;
  }
  .card {
    position: relative;
    width: 680px;
    height: 388px;
    border-radius: 26px;
    background: var(--card);
    box-shadow: 0 14px 34px rgba(0, 0, 0, 0.55);
    overflow: hidden;
  }

  /* Front */
  .front-watermark {
    position: absolute;
    right: -60px;
    top: -40px;
    width: 340px;
    height: 470px;
    border-radius: 170px 170px 0 0;
    background: radial-gradient(ellipse at 50% 40%, var(--tone-light) 0%, var(--tone-mid) 55%, transparent 75%);
  }
  .brand {
    position: absolute;
    left: 52px;
    top: 66px;
    display: flex;
    align-items: center;
    gap: 16px;
  }
  .brand-dot {
    width: 62px;
    height: 62px;
    border-radius: 50%;
    background: var(--lime);
    flex: none;
  }
  .brand-name {
    font-weight: 700;
    font-size: 40px;
    letter-spacing: 3px;
    text-transform: uppercase;
    color: var(--lime);
    line-height: 1;
  }
  .brand-region {
    font-weight: 700;
    font-size: 19px;
    letter-spacing: 4px;
    text-transform: uppercase;
    color: var(--teal);
    margin-top: 6px;
  }
  .person {
    position: absolute;
    left: 52px;
    top: 190px;
  }
  .person-name {
    font-size: 24px;
    letter-spacing: 1px;
    text-transform: uppercase;
    color: var(--teal);
  }
  .person-role {
    font-size: 17px;
    font-weight: 500;
    color: var(--text-light);
    margin-top: 2px;
  }
  .contact {
    list-style: none;
    position: absolute;
    left: 52px;
    top: 264px;
  }
  .contact li,
  .location li {
    display: flex;
    align-items: center;
    gap: 10px;
    font-size: 19px;
    color: var(--text-light);
    line-height: 30px;
  }
  .icon { width: 16px; height: 16px; flex: none; }
  .location {
    list-style: none;
    position: absolute;
    left: 400px;
    top: 186px;
  }
  .location li { align-items: flex-start; color: var(--text-soft); font-size: 17px; line-height: 25px; }
  .location .icon { margin-top: 5px; }

  /* Back */
  .card-back { background: var(--card-deep); }
  .back-pattern {
    position: absolute;
    inset: 0;
    background:
      radial-gradient(ellipse at 30% 70%, var(--tone-light) 0%, transparent 60%),
      linear-gradient(135deg, var(--tone-mid), var(--card-deep) 75%);
  }
  .back-brand {
    position: absolute;
    right: 56px;
    top: 56px;
    display: flex;
    align-items: center;
    gap: 12px;
  }
  .back-brand .brand-dot { width: 44px; height: 44px; }
  .back-brand .brand-name { font-size: 30px; }
</style>
</head>
<body>

  <section class="card card-front" aria-label="Card front">
    <div class="front-watermark" role="img" aria-label="Large faint tone-on-tone brand watermark on the right of the card"></div>

    <div class="brand">
      <span class="brand-dot" aria-hidden="true"></span>
      <div>
        <div class="brand-name">Tall Pine</div>
        <div class="brand-region">Hong Kong</div>
      </div>
    </div>

    <div class="person">
      <div class="person-name">Marcus Delaney</div>
      <div class="person-role">managing director</div>
    </div>

    <ul class="contact">
      <li>
        <svg class="icon" viewBox="0 0 16 16" aria-hidden="true"><path d="M4 1 L6.5 4.5 5 6 Q6.5 9.5 10 11 L11.5 9.5 15 12 13 15 Q6 14 1 3 Z" fill="var(--teal)"/></svg>
        852 2714 36 90
      </li>
      <li>
        <svg class="icon" viewBox="0 0 16 16" aria-hidden="true"><rect x="4" y="1" width="8" height="14" rx="1.5" fill="none" stroke="var(--teal)" stroke-width="1.8"/><circle cx="8" cy="12.3" r="0.9" fill="var(--teal)"/></svg>
        852 9382 61 47
      </li>
      <li>
        <svg class="icon" viewBox="0 0 16 16" aria-hidden="true"><rect x="1" y="3" width="14" height="10" rx="1" fill="var(--teal)"/><path d="M1.5 3.8 L8 9 14.5 3.8" fill="none" stroke="var(--card)" stroke-width="1.3"/></svg>
        mdelaney@tallpine.com
      </li>
    </ul>

    <ul class="location">
      <li>
        <svg class="icon" viewBox="0 0 16 16" aria-hidden="true"><path d="M8 15 C3 9 3 7.5 3 6 A5 5 0 0 1 13 6 C13 7.5 13 9 8 15 Z" fill="var(--teal)"/><circle cx="8" cy="6" r="1.8" fill="var(--card)"/></svg>
        <span>48 Harbour Lane, Kwun Tong<br>Kowloon 00852</span>
      </li>
      <li>
        <svg class="icon" viewBox="0 0 16 16" aria-hidden="true"><circle cx="8" cy="8" r="6.5" fill="none" stroke="var(--teal)" stroke-width="1.6"/><ellipse cx="8" cy="8" rx="2.8" ry="6.5" fill="none" stroke="var(--teal)" stroke-width="1.3"/><path d="M1.5 8 H14.5" stroke="var(--teal)" stroke-width="1.3"/></svg>
        <span>www.tallpine.com</span>
      </li>
    </ul>
  </section>

  <section class="card card-back" aria-label="Card back">
    <div class="back-pattern" role="img" aria-label="Repeating tone-on-tone brand pattern covering the whole card back"></div>
    <div class="back-brand">
      <span class="brand-dot" aria-hidden="true"></span>
      <span class="brand-name">Tall Pine</span>
    </div>
  </section>

</body>
</html>
```